Business Card for Voltrix

Horizontal business card for voltrix, the electrical contractor.
clean and professional looking, using company branding and colours.
I also want the blue in the logo and wording to be made a more 'electric' blue and the grey 'Voltrix' to be slightly darker.

Pleas use the following contact details:

Colin Marsh
Owner

t: 01736 582910
m: 07831 206719
e: colin@voltrix-installs.co.uk

www.voltrix-installs.co.uk

Industry/Entity Type

Electrical

Font styles to use
Sans Serif

```html
<!DOCTYPE html>
<html lang="en">
<head>
<meta charset="utf-8">
<title>Voltrix Business Card</title>
<link rel="stylesheet" href="https://fonts.googleapis.com/css2?family=Arimo:wght@400;700&display=swap">
<style>
  :root {
    --backdrop: #e4e5e6;
    --card: #f3f3f3;
    --brand-grey: #54585b;
    --name-grey: #4a4d50;
    --electric-blue: #1ea6d9;
    --mark-tint: #9fd6de;
    --band: #c6dcdf;
    --band-rule: #2e3032;
    --ink: #1c1d1e;
  }
  * { margin: 0; padding: 0; box-sizing: border-box; }
  html, body { width: 1200px; height: 700px; overflow: hidden; }
  body {
    background: var(--backdrop);
    font-family: "Arimo", Arial, sans-serif;
    position: relative;
  }
  .card {
    position: absolute;
    top: 205px;
    width: 500px;
    height: 290px;
    background: var(--card);
    box-shadow: 0 6px 18px rgba(0, 0, 0, 0.18);
    overflow: hidden;
  }
  .card--front { left: 70px; }
  .card--back { left: 630px; }

  /* Front */
  .brand {
    position: absolute;
    left: 26px;
    top: 78px;
  }
  .brand__row { display: flex; align-items: center; gap: 14px; }
  .brand__dot {
    width: 46px; height: 46px; border-radius: 50%;
    background: var(--mark-tint);
    flex: none;
  }
  .brand__name {
    font-size: 54px;
    font-weight: 400;
    letter-spacing: 0.2em;
    color: var(--brand-grey);
    line-height: 1;
  }
  .brand__tagline {
    margin: 6px 0 0 60px;
    font-size: 19px;
    letter-spacing: 0.07em;
    text-transform: uppercase;
    color: var(--electric-blue);
  }

  /* Back */
  .holder {
    position: absolute;
    left: 24px;
    top: 58px;
    display: flex;
    align-items: center;
    gap: 14px;
  }
  .holder__dot {
    width: 46px; height: 46px; border-radius: 50%;
    background: var(--mark-tint);
    flex: none;
  }
  .holder__name {
    font-size: 44px;
    font-weight: 400;
    color: var(--name-grey);
    word-spacing: 0.3em;
  }
  .contact-band {
    position: absolute;
    left: 0; right: 0; bottom: 0;
    height: 82px;
    background: var(--band);
    border-top: 2px solid var(--band-rule);
    padding: 12px 22px 0;
    color: var(--ink);
    font-size: 13.5px;
    line-height: 1.22;
  }
  .contact-band__list { list-style: none; }
  .contact-band__web {
    position: absolute;
    right: 22px;
    bottom: 12px;
  }
</style>
</head>
<body>
  <section class="card card--front" aria-label="Card front">
    <div class="brand">
      <div class="brand__row">
        <span class="brand__dot" aria-hidden="true"></span>
        <span class="brand__name">VOLTRIX</span>
      </div>
      <p class="brand__tagline">The Electrical Contractor</p>
    </div>
  </section>

  <section class="card card--back" aria-label="Card back">
    <div class="holder">
      <span class="holder__dot" aria-hidden="true"></span>
      <h1 class="holder__name">Colin Marsh</h1>
    </div>
    <div class="contact-band">
      <ul class="contact-band__list">
        <li>t: 01736 582910</li>
        <li>m: 07831 206719</li>
        <li>e: colin@voltrix-installs.co.uk</li>
      </ul>
      <span class="contact-band__web">www.voltrix-installs.co.uk</span>
    </div>
  </section>
</body>
</html>
```